Sales presentation introduction for Finance and Tech firms

Our business is two fold - 1) recruitment 2) consultancy. We would like a one or two page template that we can use to send to potential clients. The template will ideally be the same for the recruitment and consultancy side. We need to be able to edit the template to enter text.

I have attached our logo so you can see what we currently use on Brindlepost.

Sector is financial services and technology. We do not intent to have lots of text but the layout/images/designs to be used should cover some of page in a way that it takes up some space to avoid having to write lot of text.

Open to colour suggestions.

Please look at the attached word doc to see the text I would like for the two presentations.

Happy to answer questions.

Target Market(s)

Directors

Industry/Entity Type

Finance and tech companies

Colors
0094D4
00A9DD
6FCCEA
C7EBF8
E9F6FB

Requirements
Must have
• Editable text

```html
<!DOCTYPE html>
<html lang="en">
<head>
<meta charset="utf-8">
<title>Meridian – Consultancy &amp; Recruitment Flyers</title>
<link href="https://fonts.googleapis.com/css2?family=Oswald:wght@400;500;600&family=Roboto:wght@400;500;700&family=Roboto+Mono:wght@700&family=Montserrat:wght@400&display=swap" rel="stylesheet">
<style>
  :root{
    --navy:#0d2f6e;
    --blue:#1b4f9c;
    --bright:#0094d4;
    --cyan:#00a9dd;
    --sky:#6fccea;
    --pale:#c7ebf8;
    --mist:#e9f6fb;
    --ink:#4a4f58;
    --page:#e4e4e4;
  }
  *{margin:0;padding:0;box-sizing:border-box}
  html,body{width:677px;height:1200px;overflow:hidden;background:var(--page)}
  body{position:relative;font-family:"Roboto",sans-serif}

  .slot{position:absolute}
  .slot--hero{left:117px;top:28px;width:443px;height:615px}
  .slot--left{left:22px;top:704px;width:306px;height:424px}
  .slot--right{left:349px;top:704px;width:306px;height:424px}
  .slot--left .flyer,.slot--right .flyer{transform:scale(.69);transform-origin:0 0}

  .flyer{position:absolute;left:0;top:0;width:443px;height:615px;background:#fff;overflow:hidden;box-shadow:0 2px 6px rgba(0,0,0,.25)}
  .flyer__photo{position:absolute;left:0;top:0;width:443px;height:160px;
    background:radial-gradient(ellipse at 78% 40%,#3d86d6 0%,#1b4f9c 30%,#0a2254 65%,#050f2c 100%)}
  .brand{position:absolute;left:16px;top:72px;display:flex;align-items:center;gap:7px;color:#fff;font-family:"Montserrat",sans-serif;font-size:25px;letter-spacing:.5px}
  .brand__mark{width:12px;height:12px;background:var(--sky)}
  .flyer__banner{position:absolute;left:0;top:100px}
  .tagline{position:absolute;color:#fff;font-family:"Oswald",sans-serif;font-weight:500;font-size:11px;line-height:15.5px;text-transform:uppercase}
  .tagline--lead{left:12px;top:132px;width:200px}
  .tagline--promise{left:232px;top:165px;width:205px}

  .flyer__body{position:absolute;left:12px;top:214px;width:419px}
  .title{font-family:"Oswald",sans-serif;font-weight:500;font-size:14.5px;color:var(--blue);text-transform:uppercase}
  .copy{font-size:4.6px;line-height:7px;color:var(--ink);margin-top:6px}

  .services{position:absolute;left:0;top:296px;width:443px;height:90px}
  .service{position:absolute;top:40px;width:40px;text-align:center}
  .service__label{font-size:3.8px;line-height:4.6px;color:var(--ink);margin-top:2px}

  .section{position:absolute;width:195px}
  .section__head{display:flex;align-items:center;gap:5px;font-family:"Oswald",sans-serif;font-weight:500;font-size:13px;color:var(--blue);text-transform:uppercase}
  .section__dot{width:11px;height:11px;border-radius:50%;background:var(--blue);border:2px solid var(--pale)}
  .section .copy{margin-top:5px}

  .footer{position:absolute;left:0;top:557px;width:443px;height:58px;background:var(--pale)}
  .footer__url{position:absolute;left:0;top:0}
  .footer__url span{position:absolute;left:12px;top:4px;font-family:"Roboto Mono",monospace;font-size:12.5px;color:#fff;letter-spacing:1px}
  .footer__contact{position:absolute;left:150px;top:38px;display:flex;align-items:center;gap:5px;font-family:"Oswald",sans-serif;font-size:8.2px;color:var(--navy)}
  .footer__pin{width:8px;height:8px;border-radius:50%;background:var(--bright)}

  .pill{margin:14px auto 0;width:355px;height:32px;border-radius:16px;background:var(--blue);color:#fff;font-size:7.4px;font-weight:500;text-align:center;line-height:14px;padding-top:2px}
  .ticks{list-style:none;margin-top:10px}
  .ticks li{font-size:7px;font-weight:700;color:var(--blue);line-height:14.5px}
  .ticks li::before{content:"▲";font-size:5px;margin-right:5px;vertical-align:1px}
  .lead{font-size:7px;font-weight:700;color:var(--ink);line-height:10px;margin-top:8px;text-align:justify}
  .cloud{margin:14px auto 0;width:340px;font-family:"Oswald",sans-serif;color:var(--blue);line-height:.95;text-align:center}
  .cloud span{display:inline-block;vertical-align:middle;margin:0 1px}
  .cloud small{display:inline-block;vertical-align:middle;font-size:6px;line-height:6px;text-align:left}
</style>
</head>
<body>

<!-- Consultancy flyer, large -->
<div class="slot slot--hero">
  <article class="flyer">
    <div class="flyer__photo" role="img" aria-label="Photo of a glowing blue digital network over a dark background"></div>
    <div class="brand"><span class="brand__mark"></span>MERIDIAN</div>
    <svg class="flyer__banner" width="443" height="115" viewBox="0 100 443 115">
      <path d="M0 118 L236 118 C258 118 264 150 288 150 L443 150 L443 206 L0 206 Z" fill="#1b4f9c"/>
      <path d="M0 113 L232 113 C256 113 262 144 290 144 L443 144" fill="none" stroke="#fff" stroke-width="3"/>
      <rect x="0" y="206" width="443" height="4" fill="#6fccea"/>
    </svg>
    <p class="tagline tagline--lead">A partner who brings new and innovative ideas to the table, through extensive industry experience and knowledge.</p>
    <p class="tagline tagline--promise">Meridian will ensure you are prepared for growth.</p>

    <div class="flyer__body">
      <h2 class="title">Meridian Consultancy</h2>
      <p class="copy">Meridian E2E is a bespoke consultancy firm that specialises in buy side investment. Through an industry based consultative approach we assist our clients in preparing for and facilitating long term growth. Working closely with our clients we combine innovative thinking and breakthrough technologies to accelerate progress and, together, achieve enduring results.</p>
      <p class="copy">Experienced in successfully delivering change for global organisations as well as assisting smaller firms during their growth phase. Meridian will work with you to create a workable model and ensure successful delivery of the project.</p>
    </div>

    <div class="services">
      <svg width="443" height="40" style="position:absolute;left:0;top:0">
        <path d="M30 30 L30 14 L413 14 L413 30" fill="none" stroke="#1b4f9c" stroke-width="1"/>
        <path d="M27 28 L30 34 L33 28 Z M410 28 L413 34 L416 28 Z" fill="#1b4f9c"/>
      </svg>
      <div class="service" style="left:11px"><svg width="40" height="32"><circle cx="20" cy="16" r="15" fill="#1b4f9c" stroke="#c7ebf8" stroke-width="2"/><rect x="13" y="10" width="14" height="12" fill="none" stroke="#fff"/></svg><p class="service__label">Order Management and Trading</p></div>
      <div class="service" style="left:58px"><svg width="40" height="32"><circle cx="20" cy="16" r="15" fill="#1b4f9c" stroke="#c7ebf8" stroke-width="2"/><rect x="13" y="10" width="14" height="12" fill="none" stroke="#fff"/></svg><p class="service__label">Investment and Research</p></div>
      <div class="service" style="left:105px"><svg width="40" height="32"><circle cx="20" cy="16" r="15" fill="#1b4f9c" stroke="#c7ebf8" stroke-width="2"/><rect x="13" y="10" width="14" height="12" fill="none" stroke="#fff"/></svg><p class="service__label">Static, Pricing and Benchmark Data</p></div>
      <div class="service" style="left:152px"><svg width="40" height="32"><circle cx="20" cy="16" r="15" fill="#1b4f9c" stroke="#c7ebf8" stroke-width="2"/><rect x="12" y="11" width="16" height="10" fill="none" stroke="#fff"/></svg><p class="service__label">CRM/Onboarding</p></div>
      <div class="service" style="left:199px"><svg width="40" height="32"><circle cx="20" cy="16" r="15" fill="#1b4f9c" stroke="#c7ebf8" stroke-width="2"/><path d="M12 21 A8 8 0 0 1 28 21" fill="none" stroke="#fff"/></svg><p class="service__label">Performance, Risk and Attribution</p></div>
      <div class="service" style="left:246px"><svg width="40" height="32"><circle cx="20" cy="16" r="15" fill="#1b4f9c" stroke="#c7ebf8" stroke-width="2"/><rect x="14" y="9" width="12" height="14" fill="none" stroke="#fff"/></svg><p class="service__label">Client and Regulatory Reporting</p></div>
      <div class="service" style="left:293px"><svg width="40" height="32"><circle cx="20" cy="16" r="15" fill="#1b4f9c" stroke="#c7ebf8" stroke-width="2"/><rect x="14" y="9" width="12" height="14" fill="none" stroke="#fff"/></svg><p class="service__label">Compliance</p></div>
      <div class="service" style="left:340px"><svg width="40" height="32"><circle cx="20" cy="16" r="15" fill="#1b4f9c" stroke="#c7ebf8" stroke-width="2"/><rect x="13" y="10" width="14" height="12" fill="none" stroke="#fff"/></svg><p class="service__label">Finance and Accounting</p></div>
      <div class="service" style="left:393px"><svg width="40" height="32"><circle cx="20" cy="16" r="15" fill="#1b4f9c" stroke="#c7ebf8" stroke-width="2"/><rect x="13" y="11" width="14" height="11" fill="none" stroke="#fff"/></svg><p class="service__label">Middle and Back Office</p></div>
    </div>

    <section class="section" style="left:14px;top:408px">
      <h3 class="section__head"><span class="section__dot"></span>Business Strategy</h3>
      <p class="copy">Meridian will help you create a business strategy tailored to your requirements. Ensuring each business process is defined and taken into account allows for a successful design. Creating and implementing an operating model that takes into account budget, resources, culture and your company's vision.</p>
    </section>
    <section class="section" style="left:232px;top:408px">
      <h3 class="section__head"><span class="section__dot"></span>Change Management</h3>
      <p class="copy">Meridian works with clients to deliver bespoke change initiatives. Rigorous business analysis and risk management allows for successful change initiatives. We work with you throughout the complete process, to ensure that delivery is based on value. Transition phases are challenging aspects of change initiatives which is why our team manage all transitions and the risk they carry.</p>
    </section>
    <section class="section" style="left:14px;top:490px">
      <h3 class="section__head"><span class="section__dot"></span>IT Transformation</h3>
      <p class="copy">Meridian is widely experienced in a range of technologies. We help with the implementation of software provider or design and develop bespoke services. Covering front to back office the team specialises in full project lifecycle from feasibility through to implementation.</p>
    </section>
    <section class="section" style="left:232px;top:490px">
      <h3 class="section__head"><span class="section__dot"></span>Organisational Structure</h3>
      <p class="copy">Meridian works with clients to improve resource capability and strategic partnerships. Acting as an extension of the HR function, we analyse business processes and ensure that our clients have the ability to manage changing workforce demands.</p>
    </section>

    <footer class="footer">
      <svg class="footer__url" width="200" height="26"><path d="M0 0 L178 0 L196 24 L0 24 Z" fill="#1b4f9c"/></svg>
      <div class="footer__url"><span>www.meridiane2e.com</span></div>
      <p class="footer__contact"><span class="footer__pin"></span>London,United Kingdom | info@meridiane2e.com | +44 (0) 7700 900123</p>
    </footer>
  </article>
</div>

<!-- Consultancy flyer, small -->
<div class="slot slot--left">
  <article class="flyer">
    <div class="flyer__photo" role="img" aria-label="Photo of a glowing blue digital network over a dark background"></div>
    <div class="brand"><span class="brand__mark"></span>MERIDIAN</div>
    <svg class="flyer__banner" width="443" height="115" viewBox="0 100 443 115">
      <path d="M0 118 L236 118 C258 118 264 150 288 150 L443 150 L443 206 L0 206 Z" fill="#1b4f9c"/>
      <path d="M0 113 L232 113 C256 113 262 144 290 144 L443 144" fill="none" stroke="#fff" stroke-width="3"/>
      <rect x="0" y="206" width="443" height="4" fill="#6fccea"/>
    </svg>
    <p class="tagline tagline--lead">A partner who brings new and innovative ideas to the table, through extensive industry experience and knowledge.</p>
    <p class="tagline tagline--promise">Meridian will ensure you are prepared for growth.</p>

    <div class="flyer__body">
      <h2 class="title">Meridian Consultancy</h2>
      <p class="copy">Meridian E2E is a bespoke consultancy firm that specialises in buy side investment. Through an industry based consultative approach we assist our clients in preparing for and facilitating long term growth. Working closely with our clients we combine innovative thinking and breakthrough technologies to accelerate progress and, together, achieve enduring results.</p>
      <p class="copy">Experienced in successfully delivering change for global organisations as well as assisting smaller firms during their growth phase. Meridian will work with you to create a workable model and ensure successful delivery of the project.</p>
    </div>

    <div class="services">
      <svg width="443" height="40" style="position:absolute;left:0;top:0">
        <path d="M30 30 L30 14 L413 14 L413 30" fill="none" stroke="#1b4f9c" stroke-width="1"/>
        <path d="M27 28 L30 34 L33 28 Z M410 28 L413 34 L416 28 Z" fill="#1b4f9c"/>
      </svg>
      <div class="service" style="left:11px"><svg width="40" height="32"><circle cx="20" cy="16" r="15" fill="#1b4f9c" stroke="#c7ebf8" stroke-width="2"/><rect x="13" y="10" width="14" height="12" fill="none" stroke="#fff"/></svg><p class="service__label">Order Management and Trading</p></div>
      <div class="service" style="left:58px"><svg width="40" height="32"><circle cx="20" cy="16" r="15" fill="#1b4f9c" stroke="#c7ebf8" stroke-width="2"/><rect x="13" y="10" width="14" height="12" fill="none" stroke="#fff"/></svg><p class="service__label">Investment and Research</p></div>
      <div class="service" style="left:105px"><svg width="40" height="32"><circle cx="20" cy="16" r="15" fill="#1b4f9c" stroke="#c7ebf8" stroke-width="2"/><rect x="13" y="10" width="14" height="12" fill="none" stroke="#fff"/></svg><p class="service__label">Static, Pricing and Benchmark Data</p></div>
      <div class="service" style="left:152px"><svg width="40" height="32"><circle cx="20" cy="16" r="15" fill="#1b4f9c" stroke="#c7ebf8" stroke-width="2"/><rect x="12" y="11" width="16" height="10" fill="none" stroke="#fff"/></svg><p class="service__label">CRM/Onboarding</p></div>
      <div class="service" style="left:199px"><svg width="40" height="32"><circle cx="20" cy="16" r="15" fill="#1b4f9c" stroke="#c7ebf8" stroke-width="2"/><path d="M12 21 A8 8 0 0 1 28 21" fill="none" stroke="#fff"/></svg><p class="service__label">Performance, Risk and Attribution</p></div>
      <div class="service" style="left:246px"><svg width="40" height="32"><circle cx="20" cy="16" r="15" fill="#1b4f9c" stroke="#c7ebf8" stroke-width="2"/><rect x="14" y="9" width="12" height="14" fill="none" stroke="#fff"/></svg><p class="service__label">Client and Regulatory Reporting</p></div>
      <div class="service" style="left:293px"><svg width="40" height="32"><circle cx="20" cy="16" r="15" fill="#1b4f9c" stroke="#c7ebf8" stroke-width="2"/><rect x="14" y="9" width="12" height="14" fill="none" stroke="#fff"/></svg><p class="service__label">Compliance</p></div>
      <div class="service" style="left:340px"><svg width="40" height="32"><circle cx="20" cy="16" r="15" fill="#1b4f9c" stroke="#c7ebf8" stroke-width="2"/><rect x="13" y="10" width="14" height="12" fill="none" stroke="#fff"/></svg><p class="service__label">Finance and Accounting</p></div>
      <div class="service" style="left:393px"><svg width="40" height="32"><circle cx="20" cy="16" r="15" fill="#1b4f9c" stroke="#c7ebf8" stroke-width="2"/><rect x="13" y="11" width="14" height="11" fill="none" stroke="#fff"/></svg><p class="service__label">Middle and Back Office</p></div>
    </div>

    <section class="section" style="left:14px;top:408px">
      <h3 class="section__head"><span class="section__dot"></span>Business Strategy</h3>
      <p class="copy">Meridian will help you create a business strategy tailored to your requirements. Ensuring each business process is defined and taken into account allows for a successful design. Creating and implementing an operating model that takes into account budget, resources, culture and your company's vision.</p>
    </section>
    <section class="section" style="left:232px;top:408px">
      <h3 class="section__head"><span class="section__dot"></span>Change Management</h3>
      <p class="copy">Meridian works with clients to deliver bespoke change initiatives. Rigorous business analysis and risk management allows for successful change initiatives. We work with you throughout the complete process, to ensure that delivery is based on value. Transition phases are challenging aspects of change initiatives which is why our team manage all transitions and the risk they carry.</p>
    </section>
    <section class="section" style="left:14px;top:490px">
      <h3 class="section__head"><span class="section__dot"></span>IT Transformation</h3>
      <p class="copy">Meridian is widely experienced in a range of technologies. We help with the implementation of software provider or design and develop bespoke services. Covering front to back office the team specialises in full project lifecycle from feasibility through to implementation.</p>
    </section>
    <section class="section" style="left:232px;top:490px">
      <h3 class="section__head"><span class="section__dot"></span>Organisational Structure</h3>
      <p class="copy">Meridian works with clients to improve resource capability and strategic partnerships. Acting as an extension of the HR function, we analyse business processes and ensure that our clients have the ability to manage changing workforce demands.</p>
    </section>

    <footer class="footer">
      <svg class="footer__url" width="200" height="26"><path d="M0 0 L178 0 L196 24 L0 24 Z" fill="#1b4f9c"/></svg>
      <div class="footer__url"><span>www.meridiane2e.com</span></div>
      <p class="footer__contact"><span class="footer__pin"></span>London,United Kingdom | info@meridiane2e.com | +44 (0) 7700 900123</p>
    </footer>
  </article>
</div>

<!-- Recruitment flyer, small -->
<div class="slot slot--right">
  <article class="flyer">
    <div class="flyer__photo" role="img" aria-label="Photo of a glowing blue digital network over a dark background"></div>
    <div class="brand"><span class="brand__mark"></span>MERIDIAN</div>
    <svg class="flyer__banner" width="443" height="115" viewBox="0 100 443 115">
      <path d="M0 118 L236 118 C258 118 264 150 288 150 L443 150 L443 206 L0 206 Z" fill="#1b4f9c"/>
      <path d="M0 113 L232 113 C256 113 262 144 290 144 L443 144" fill="none" stroke="#fff" stroke-width="3"/>
      <rect x="0" y="206" width="443" height="4" fill="#6fccea"/>
    </svg>
    <p class="tagline tagline--lead">A partner who brings new and innovative ideas to the table, through extensive industry experience and knowledge.</p>
    <p class="tagline tagline--promise">Meridian will ensure you are prepared for growth.</p>

    <div class="flyer__body">
      <h2 class="title">Meridian Recruitment</h2>
      <p class="copy">Meridian is more than an ordinary recruitment service. Our experts work with clients to develop a HR strategy that maps current and impending organisational needs, using research to effectively benchmark. We are developing various talent communities that provide effective and timely recruitment solutions for our clients.</p>
      <p class="copy">Specialists in Asset Management recruitment with a specialisation in IT, Operations, Regulation and Change Management.</p>
      <p class="copy">Meridian acts as an extension of your HR function, providing an end-to-end permanent and contingent talent acquisition solution, taking full accountability and ownership for the entire recruitment process, which includes:</p>
      <div class="pill">▲ Workforce Planning &nbsp;▲ Strategic Sourcing &nbsp;▲ Talent Engagement<br>▲ Candidate Management &nbsp;▲ Weekly Vacancy Updates</div>
      <p class="copy" style="margin-top:12px">We recognise that hiring can be a lengthy process, therefore we partner with you to ensure you only interview top quantile candidates, cutting out multiple meetings with multiple candidates. Giving hiring managers time back in their diaries to do their day jobs and reducing the time to hire. This is achieved by:</p>
      <ul class="ticks">
        <li>Understanding the roles, and partnering with you to build meaningful job descriptions</li>
        <li>Candidates are fully screened and interviewed prior to presentation to you</li>
        <li>Qualified shortlist of top 3 candidates</li>
        <li>Support with interviews and we ensure the candidate has a positive experience</li>
      </ul>
      <p class="lead">Meridian recruitment partners with principal business consultants from Meridian consultancy to ensure candidates are properly screened before presenting to our clients. This allows for our clients to focus on only interviewing the best on the market.</p>
      <div class="cloud">
        <span style="font-size:15px">FIXED INCOME</span><span style="font-size:15px">BUSINESS INTELLIGENCE</span><span style="font-size:10px">RISK AND ATTRIBUTION</span><br>
        <span style="font-size:13px">FIX/WIRE</span><span style="font-size:9px">EQUITY</span><span style="font-size:30px">SQL</span><span style="font-size:12px">SETTLEMENT</span><span style="font-size:10px">LEDGER</span><span style="font-size:11px">REFERENCE DATA</span><br>
        <span style="font-size:10px">COLLATERAL<br>MANAGEMENT</span><span style="font-size:26px">MIS</span><span style="font-size:10px">CONNECTIVITY<br>PRICING AND ANALYTICS</span><span style="font-size:28px">XML</span><span style="font-size:12px">BATCH <small>WORKFLOW<br>MANAGEMENT</small><br>PROCESSING</span>
      </div>
    </div>

    <footer class="footer">
      <svg class="footer__url" width="200" height="26"><path d="M0 0 L178 0 L196 24 L0 24 Z" fill="#1b4f9c"/></svg>
      <div class="footer__url"><span>www.meridiane2e.com</span></div>
      <p class="footer__contact"><span class="footer__pin"></span>London,United Kingdom | info@meridiane2e.com | +44 (0) 7700 900123</p>
    </footer>
  </article>
</div>

</body>
</html>
```